Website redesign for KeelFundPal/CamperCashMate

Job Title: Talented Web Designer for SEO-Friendly Website Creation & NestHostly cPanel Integration
 
Inspiration: dunetrackrally.example
Pages:

About
Get a Quote
FAQ
Boat Loans
RV Loans
Testimonials
News/Blog
Affiliate Program
Contact

Job Description:
 
We are seeking a skilled and creative freelance web designer to build a stunning, SEO-optimized website for our business. The ideal candidate will have a strong design portfolio, technical expertise in creating search engine-friendly websites, and experience implementing websites into NestHostly cPanel.
 
Project Overview:
 
Objective: Create a modern, motorsports themed visually appealing website that is optimized for SEO.

Platform: The site will be hosted on NestHostly, so familiarity with their cPanel for setup and integration is essential.

Deliverables:
         •A fully functional website (desktop and mobile) with user-friendly navigation and a responsive design.
         •SEO best practices implemented throughout, including proper meta tags, optimized images, fast loading speeds, and mobile compatibility.
         •Seamless integration into NestHostly cPanel for hosting.
         •Guidance or documentation on maintaining the site post-launch.
 
Key Skills Required:
 
         •Proficiency in web design (HTML, CSS, JavaScript, or relevant platforms like WordPress).
         •Knowledge of SEO principles and tools for website optimization.
         •Experience with NestHostly cPanel, including file management and DNS settings.
         •Strong communication skills to understand our vision and provide progress updates.
 
What We’re Looking For:
 
         •A designer who can transform our ideas into a sleek and functional website.
         •Someone proactive in suggesting creative design elements and SEO improvements.
         •A reliable professional who can meet deadlines and deliver a polished product.
 
Please provide:
 
         1.A brief introduction and why you’re a good fit for this project.
         2.Examples of previous web design projects, especially those with SEO implementation.
         3.Your estimated timeline and cost for this project.
 
We are excited to work with a talented designer who can bring our vision to life. If you are passionate about web design and SEO, we’d love to hear from you!

Target Market(s)

Boat and RV buyers looking for a loan

Coding

Number of Pages Required

5+ page

Colors
F0912C
F2A743
F7CA91
FBE8D2
FDF5EE

Requirements
Must have
• motorsports type design
Nice to have
• fcontact forms easy to use layout on brand and color scheme of keelfundpal and campercashmate.example

```html
<!DOCTYPE html>
<html lang="en">
<head>
<meta charset="utf-8">
<title>CamperCashMate – RV Loans Made Easy</title>
<link href="https://fonts.googleapis.com/css2?family=Outfit:wght@400;500;600&family=Roboto:wght@400;500;700&display=swap" rel="stylesheet">
<style>
:root{
  --orange:#F0912C;
  --orange-2:#F2A743;
  --orange-3:#F7CA91;
  --cream:#FBE8D2;
  --cream-2:#FDF5EE;
  --blue:#1a8cf0;
  --blue-dark:#0f6fcc;
  --ink:#1d1d1d;
  --text:#333;
  --nav:#4f4f4f;
  --grey:#f4f5f7;
}
*{box-sizing:border-box;margin:0;padding:0}
html,body{width:1200px;height:4130px;overflow:hidden}
body{font-family:Roboto,Arial,sans-serif;color:var(--text);background:#fff;position:relative}
.abs{position:absolute}
h1,h2,h3{font-family:Outfit,Arial,sans-serif;font-weight:500;color:var(--ink)}
.btn{position:absolute;display:flex;align-items:center;justify-content:center;background:var(--orange);color:#fff;font:500 14px Roboto,sans-serif;text-transform:uppercase;border-radius:3px}

/* header */
.header{position:absolute;left:0;top:0;width:1200px;height:144px}
.brand{position:absolute;left:112px;top:28px;font:600 30px Outfit,sans-serif;color:var(--orange);display:flex;align-items:center;gap:10px}
.brand .dot{width:26px;height:26px;border-radius:50%;background:var(--blue)}
.apply-top{position:absolute;left:652px;top:30px;width:120px;height:42px;background:#fff;box-shadow:0 2px 10px rgba(0,0,0,.12);color:var(--blue);font:500 13px Roboto,sans-serif;display:flex;align-items:center;justify-content:center}
.socials{position:absolute;left:803px;top:36px;display:flex;gap:10px}
.socials span{width:30px;height:30px;border-radius:50%;background:#eee}
.socials span:first-child{background:var(--orange)}
.navbar{position:absolute;left:0;top:99px;width:1200px;height:45px;background:var(--nav)}
.nav{position:absolute;left:96px;top:99px;height:45px;display:flex;align-items:center}
.nav a{color:#fff;font:500 13px Roboto,sans-serif;text-decoration:none;padding:0 14px;border-left:1px solid rgba(255,255,255,.25);text-transform:uppercase}
.nav a:first-child{border-left:0;color:var(--orange);text-decoration:underline}
.callbox{position:absolute;left:953px;top:0;width:247px;height:144px;background:var(--orange);clip-path:polygon(18% 0,100% 0,100% 100%,0 100%)}
.callbox .lbl{position:absolute;left:88px;top:46px;color:#fff;font:500 11px Roboto,sans-serif;display:flex;align-items:center;gap:10px}
.callbox .lbl i{width:30px;height:30px;border-radius:50%;background:#fff;display:flex;align-items:center;justify-content:center}
.callbox .num{position:absolute;left:64px;top:82px;color:#fff;font:600 24px Roboto,sans-serif}

/* hero */
.hero-img{position:absolute;left:0;top:144px;width:1200px;height:608px;background:linear-gradient(160deg,#5b8fd6 0%,#8fb6e6 40%,#c7cdd4 60%,#6a6e74 100%)}
.hero-title{position:absolute;left:107px;top:256px;color:#fff;font-size:48px;line-height:54px;font-weight:500}
.hero-text{position:absolute;left:112px;top:374px;width:330px;color:#fff;font-size:18px;line-height:29px}
.dots{position:absolute;left:554px;top:667px;display:flex;gap:13px}
.dots span{width:12px;height:12px;border:2px solid #fff}
.dots span.on{background:#fff}

/* trusted */
.frame{position:absolute;left:110px;top:1012px;width:358px;height:318px;border:10px solid #e4e4e4}
.frame-cut{position:absolute;left:120px;top:1000px;width:360px;height:20px;background:#fff}
.photo{position:absolute}
.trusted-title{position:absolute;left:649px;top:830px;width:330px;font-size:36px;line-height:47px}
.bar{position:absolute;height:4px;background:var(--blue)}
.bullets{position:absolute;left:649px;top:1002px;list-style:none}
.bullets li{font-size:14px;line-height:27.5px;color:#222;padding-left:24px;position:relative}
.bullets li::before{content:"";position:absolute;left:0;top:12px;width:4px;height:4px;background:var(--orange)}
.trusted-text{position:absolute;left:649px;top:1180px;width:440px;font-size:14px;line-height:25px;color:#444}

/* orange band */
.band{position:absolute;left:0;top:1378px;width:1200px;height:684px;background:linear-gradient(180deg,var(--orange) 0%,#eb8a25 60%,var(--orange-2) 100%)}
.band-title{position:absolute;left:0;width:1200px;top:1508px;text-align:center;color:#fff;font-size:38px;line-height:46px}
.band-sub{position:absolute;left:0;width:1200px;top:1637px;text-align:center;color:#fff;font-size:16px}
.card{position:absolute;top:1701px;width:301px;height:237px;border:4px solid #fff;border-radius:20px;overflow:hidden}
.card-lbl{position:absolute;top:1962px;width:301px;text-align:center;color:#fff;font:500 18px Roboto,sans-serif;text-transform:uppercase}

/* types */
.types-title{position:absolute;left:0;width:1200px;top:2165px;text-align:center;font-size:34px}
.dia{position:absolute;width:150px;height:150px;transform:rotate(45deg);background:#fff;border-radius:16px;box-shadow:0 6px 24px rgba(20,60,120,.12)}
.dia.active{border:3px solid var(--orange)}
.dia.apply{background:var(--orange);box-shadow:0 8px 24px rgba(240,145,44,.35)}
.type{position:absolute;width:160px;text-align:center;color:var(--orange);font:500 15px Roboto,sans-serif;line-height:20px;text-transform:uppercase}
.type .ico{display:block;margin:0 auto 10px;width:104px;height:48px;background:var(--blue);border-radius:8px}
.type.apply{color:#fff;font-size:17px;font-weight:700}

/* testimonials */
.say{position:absolute;left:0;top:2723px;width:1200px;height:564px;background:var(--grey)}
.say-title{position:absolute;left:0;width:1200px;top:2800px;text-align:center;font-size:40px}
.tcard{position:absolute;left:293px;top:2903px;width:713px;height:296px;background:#fff;border-radius:22px;box-shadow:0 8px 30px rgba(0,0,0,.08)}
.avatar{position:absolute;left:193px;top:2955px;width:200px;height:200px;border-radius:50%;border:4px solid var(--orange);background:#fff;padding:8px}
.avatar div{width:100%;height:100%;border-radius:50%;background:linear-gradient(180deg,#3f6a3a,#7aa6c8)}
.quote{position:absolute;left:438px;top:2940px;width:518px;font-size:12.5px;line-height:20px;color:#444;text-align:justify}
.who{position:absolute;left:438px;top:3106px;color:var(--blue);font:500 17px Roboto,sans-serif}
.stars{position:absolute;left:438px;top:3134px;color:var(--orange);font-size:16px;letter-spacing:2px}
.qmark{position:absolute;left:906px;top:3110px;font:700 80px Georgia,serif;color:#e6e6e6;line-height:80px}

/* contact */
.contact{position:absolute;left:0;top:3287px;width:1200px;height:480px;background:linear-gradient(180deg,var(--blue) 0%,#2b96f2 60%,var(--blue) 100%)}
.contact-title{position:absolute;left:153px;top:3366px;color:#fff;font-size:40px;line-height:48px}
.cline{position:absolute;left:406px;top:3390px;width:74px;height:4px;background:var(--orange)}
.citem{position:absolute;left:153px;display:flex;gap:14px}
.citem i{width:48px;height:48px;background:#fff;border-radius:4px;display:flex;align-items:center;justify-content:center}
.citem b{display:block;color:#fff;font:500 19px Roboto,sans-serif;margin-top:4px}
.citem span{color:#fff;font-size:15px}
.calc{position:absolute;left:590px;top:3372px;width:456px;height:233px;border:2px solid var(--orange)}
.select{position:absolute;left:612px;width:412px;height:45px;background:#fff;border-radius:2px;font-size:13px;color:#333;padding-left:16px;display:flex;align-items:center}
.select svg{position:absolute;right:16px;top:15px}

/* footer */
.footer{position:absolute;left:0;top:3749px;width:1200px;height:381px;background:var(--cream-2)}
.fbrand{position:absolute;left:112px;top:3922px;font:600 30px Outfit,sans-serif;color:var(--orange);display:flex;align-items:center;gap:10px}
.fbrand .dot{width:26px;height:26px;border-radius:50%;background:var(--blue)}
.fh{position:absolute;top:3837px;font:700 14px Roboto,sans-serif;color:#111;text-transform:uppercase}
.fitem{position:absolute;display:flex;gap:12px;font-size:12px;line-height:17px;color:#333}
.fitem i{flex:0 0 26px;width:26px;height:26px;border-radius:50%;background:var(--orange);display:flex;align-items:center;justify-content:center}
.fmenu{position:absolute;left:760px;top:3874px;list-style:none;font-size:11px;line-height:19px;color:#333}
.fsoc{position:absolute;left:966px;display:flex;gap:12px;font-size:12px;line-height:15px;color:#222}
.fsoc i{width:22px;height:22px;border-radius:50%;background:var(--orange);flex:0 0 22px}
.fline{position:absolute;left:100px;top:4066px;width:1000px;height:1px;background:#bbb}
.copy{position:absolute;left:0;width:1200px;top:4088px;text-align:center;font-size:11px;color:#333}
.totop{position:absolute;left:988px;top:4053px;width:114px;height:32px;border-radius:16px;background:var(--blue);color:#fff;font:500 11px Roboto,sans-serif;display:flex;align-items:center;justify-content:center;gap:6px}
.tag{position:absolute;left:1133px;top:4094px;font-size:9px;color:#555}
</style>
</head>
<body>

<!-- Header -->
<header class="header">
  <div class="brand"><span class="dot"></span>CamperCashMate</div>
  <div class="apply-top">APPLY NOW</div>
  <div class="socials"><span></span><span></span><span></span><span></span></div>
</header>
<div class="navbar"></div>
<nav class="nav">
  <a>Home</a><a>About</a><a>FAQ</a><a>Boat Loans</a><a>RV Loans</a><a>Testimonials</a><a>Blog</a><a>Affiliate Program</a><a>Contact</a>
</nav>
<div class="callbox">
  <div class="lbl"><i><svg width="14" height="14" viewBox="0 0 24 24"><path fill="#F0912C" d="M6.6 10.8a15 15 0 0 0 6.6 6.6l2.2-2.2c.3-.3.7-.4 1-.2 1.1.4 2.3.6 3.6.6.6 0 1 .4 1 1V20c0 .6-.4 1-1 1A17 17 0 0 1 3 4c0-.6.4-1 1-1h3.5c.6 0 1 .4 1 1 0 1.3.2 2.5.6 3.6.1.3 0 .7-.2 1z"/></svg></i>CALL US TODAY!</div>
  <div class="num">555-014-2277</div>
</div>

<!-- Hero -->
<section>
  <div class="hero-img" role="img" aria-label="Pickup truck towing a large fifth-wheel RV trailer in a parking lot under a blue sky"></div>
  <svg class="abs" style="left:0;top:600px" width="1200" height="160" viewBox="0 0 1200 160">
    <path d="M0 12 Q300 70 600 152 Q900 60 1200 -10 L1200 160 L0 160Z" fill="#fff"/>
    <path d="M0 12 Q300 70 600 152 Q900 60 1200 -10 L1200 10 Q900 90 600 150 Q300 80 0 30Z" fill="#1a8cf0"/>
    <path d="M0 30 Q300 95 600 152 Q300 110 0 60Z" fill="#1a8cf0"/>
  </svg>
  <h1 class="hero-title">RV LOANS<br>MADE EASY!</h1>
  <p class="hero-text">Welcome to CamperCashMate.com, your one-stop resource for all of your RV financing needs.</p>
  <div class="btn" style="left:112px;top:481px;width:142px;height:48px">Apply Today</div>
  <div class="dots"><span></span><span class="on"></span><span></span><span></span></div>
</section>

<!-- Trusted source -->
<section>
  <div class="frame"></div>
  <div class="frame-cut"></div>
  <div class="photo" style="left:187px;top:851px;width:298px;height:334px;background:linear-gradient(180deg,#4a8fe0 0%,#c9a77a 35%,#2fa7a0 70%,#1d8e8e 100%)" role="img" aria-label="Pontoon boat with people on turquoise lake water"></div>
  <div class="photo" style="left:343px;top:1014px;width:236px;height:261px;border:6px solid #fff;background:linear-gradient(180deg,#79a9d8 0%,#d6d2c8 45%,#5c8f3a 100%)" role="img" aria-label="Class A motorhome parked on green grass"></div>
  <h2 class="trusted-title">YOUR TRUSTED SOURCE FOR RV FINANCING.</h2>
  <div class="bar" style="left:649px;top:970px;width:76px"></div>
  <ul class="bullets">
    <li>Loans from $25,000 - $5M</li>
    <li>Up to 25yrs old</li>
    <li>Same-Day Approvals</li>
    <li>Quick Funding</li>
    <li>Private Party or Dealer</li>
    <li>Best Rates in the Industry</li>
  </ul>
  <p class="trusted-text">Our goal is to make your RV purchase as quick and stress-free as possible. Our numerous lender relationships allow us to offer competitive rates and terms with quick turn-around times.</p>
  <div class="btn" style="left:649px;top:1282px;width:142px;height:48px">Learn More</div>
</section>

<!-- Financing band -->
<section>
  <div class="band" role="img" aria-label="Orange band with a faint marina backdrop"></div>
  <svg class="abs" style="left:0;top:1370px" width="1200" height="60" viewBox="0 0 1200 60">
    <path d="M0 0 H1200 V40 Q1050 10 900 30 Q750 0 600 26 Q450 4 300 30 Q150 10 0 34Z" fill="#fff"/>
  </svg>
  <h2 class="band-title">WE FINANCE MORE THAN<br>JUST BOATS</h2>
  <div class="band-sub">At Harborline Recreational Finance, we are your one-stop resource for all marine, RV and Airplane Financing</div>
  <div class="card" style="left:112px;background:linear-gradient(180deg,#7aa2a0 0%,#4d7fa6 50%,#cfe0ea 100%)" role="img" aria-label="Wake boat speeding across a lake"></div>
  <div class="card" style="left:449px;background:linear-gradient(180deg,#5d97e0 0%,#b9c1c9 55%,#5a5e63 100%)" role="img" aria-label="Pickup truck towing a fifth-wheel RV"></div>
  <div class="card" style="left:787px;background:linear-gradient(180deg,#3c9be6 0%,#bfe0f5 55%,#b7b2a6 100%)" role="img" aria-label="Private jet parked on the tarmac with stairs down"></div>
  <div class="card-lbl" style="left:112px">Marine Financing</div>
  <div class="card-lbl" style="left:449px;text-decoration:underline">RV Financing</div>
  <div class="card-lbl" style="left:787px">Aircraft Financing</div>
</section>

<!-- RV types -->
<section>
  <h2 class="types-title">WE FINANCE ALL TYPES OF RV’S</h2>
  <div class="bar" style="left:563px;top:2211px;width:74px"></div>

  <div class="dia" style="left:164px;top:2290px"></div>
  <div class="dia active" style="left:404px;top:2290px"></div>
  <div class="dia" style="left:644px;top:2290px"></div>
  <div class="dia" style="left:886px;top:2290px"></div>
  <div class="dia" style="left:284px;top:2432px"></div>
  <div class="dia" style="left:524px;top:2432px"></div>
  <div class="dia apply" style="left:764px;top:2432px"></div>

  <div class="type" style="left:159px;top:2318px"><span class="ico" role="img" aria-label="Diesel pusher motorhome icon"></span>Diesel<br>Pushers</div>
  <div class="type" style="left:399px;top:2318px"><span class="ico" role="img" aria-label="Class A motorhome icon"></span>Class A</div>
  <div class="type" style="left:639px;top:2318px"><span class="ico" role="img" aria-label="Class B camper van icon"></span>Class B</div>
  <div class="type" style="left:881px;top:2318px"><span class="ico" role="img" aria-label="Class C motorhome icon"></span>Class C</div>
  <div class="type" style="left:279px;top:2460px"><span class="ico" style="width:52px" role="img" aria-label="Toy hauler icon"></span>Toy<br>Haulers</div>
  <div class="type" style="left:519px;top:2460px"><span class="ico" role="img" aria-label="Travel trailer icon"></span>Travel<br>Trailers</div>
  <div class="type apply" style="left:759px;top:2496px">Apply Now</div>
</section>

<!-- Testimonials -->
<section>
  <div class="say"></div>
  <h2 class="say-title">WHAT OUR CUSTOMERS SAY</h2>
  <div class="bar" style="left:563px;top:2853px;width:74px"></div>
  <svg class="abs" style="left:64px;top:3030px" width="50" height="30" viewBox="0 0 50 30"><path d="M48 15H4M16 3 4 15l12 12" stroke="#888" stroke-width="2" fill="none"/></svg>
  <svg class="abs" style="left:1086px;top:3030px" width="50" height="30" viewBox="0 0 50 30"><path d="M2 15h44M34 3l12 12-12 12" stroke="#888" stroke-width="2" fill="none"/></svg>
  <div class="tcard"></div>
  <div class="avatar"><div role="img" aria-label="Customer portrait outdoors"></div></div>
  <p class="quote">"Just purchased a boat and used Harborline and they made the process very easy. Tessa Lindqvist helped every step of the way and was always available when I had any questions. She was quick to keep me updated and streamlined the entire process of paperwork and funding. I would highly recommend using Harborline based on my purchasing experience. Ask for Tessa and she will not let you down will definitely use again when buying my next boat. Just purchased a boat and used Harborline and they made the process very easy...</p>
  <div class="who">- DALE MORROW</div>
  <div class="stars">★★★★★</div>
  <div class="qmark">”</div>
</section>

<!-- Contact -->
<section>
  <div class="contact" role="img" aria-label="Blue-tinted backdrop of a stone bridge over water"></div>
  <svg class="abs" style="left:0;top:3700px" width="1200" height="70" viewBox="0 0 1200 70">
    <path d="M0 40 Q150 20 300 42 Q450 62 600 36 Q750 14 900 40 Q1050 60 1200 30 V70 H0Z" fill="#FDF5EE"/>
  </svg>
  <h2 class="contact-title">CONTACT US</h2>
  <div class="cline"></div>
  <div class="citem" style="top:3440px"><i><svg width="20" height="20" viewBox="0 0 24 24"><path fill="#F0912C" d="M6.6 10.8a15 15 0 0 0 6.6 6.6l2.2-2.2c.3-.3.7-.4 1-.2 1.1.4 2.3.6 3.6.6.6 0 1 .4 1 1V20c0 .6-.4 1-1 1A17 17 0 0 1 3 4c0-.6.4-1 1-1h3.5c.6 0 1 .4 1 1 0 1.3.2 2.5.6 3.6.1.3 0 .7-.2 1z"/></svg></i><div><b>PHONE:</b><span>(555) 014-2277</span></div></div>
  <div class="citem" style="top:3530px"><i><svg width="20" height="20" viewBox="0 0 24 24"><path fill="#F0912C" d="M2 5h20v14H2z"/><path d="M2 5l10 8 10-8" stroke="#fff" stroke-width="2" fill="none"/></svg></i><div><b>EMAIL:</b><span>reid@campercashmate.example</span></div></div>
  <div class="calc"></div>
  <div class="select" style="top:3404px">Loan Amount<svg width="8" height="14" viewBox="0 0 8 14"><path d="M4 1 7 5H1zM4 13 1 9h6z" fill="#333"/></svg></div>
  <div class="select" style="top:3465px">Rate (APR)<svg width="8" height="14" viewBox="0 0 8 14"><path d="M4 1 7 5H1zM4 13 1 9h6z" fill="#333"/></svg></div>
  <div class="select" style="top:3526px">Term (Years)<svg width="8" height="14" viewBox="0 0 8 14"><path d="M4 1 7 5H1zM4 13 1 9h6z" fill="#333"/></svg></div>
  <div class="btn" style="left:716px;top:3584px;width:202px;height:48px">Calculate Payment</div>
</section>

<!-- Footer -->
<footer>
  <div class="footer"></div>
  <div class="fbrand"><span class="dot"></span>CamperCashMate</div>

  <div class="fh" style="left:489px">Contact</div>
  <div class="fitem" style="left:489px;top:3878px"><i><svg width="12" height="14" viewBox="0 0 24 28"><path fill="#fff" d="M12 0a10 10 0 0 0-10 10c0 7 10 18 10 18s10-11 10-18A10 10 0 0 0 12 0zm0 14a4 4 0 1 1 0-8 4 4 0 0 1 0 8z"/></svg></i><div>410 Alder Bend Rd, Ste.<br>12, Fairview, CA 90000</div></div>
  <div class="fitem" style="left:489px;top:3935px"><i><svg width="12" height="12" viewBox="0 0 24 24"><path fill="#fff" d="M6.6 10.8a15 15 0 0 0 6.6 6.6l2.2-2.2c.3-.3.7-.4 1-.2 1.1.4 2.3.6 3.6.6.6 0 1 .4 1 1V20c0 .6-.4 1-1 1A17 17 0 0 1 3 4c0-.6.4-1 1-1h3.5c.6 0 1 .4 1 1 0 1.3.2 2.5.6 3.6.1.3 0 .7-.2 1z"/></svg></i><div>Call Us<br>(555) 014-2277</div></div>
  <div class="fitem" style="left:489px;top:3992px"><i><svg width="12" height="10" viewBox="0 0 24 18"><path fill="#fff" d="M0 0h24v18H0z"/><path d="M0 0l12 9 12-9" stroke="#F0912C" stroke-width="2" fill="none"/></svg></i><div>E mail Us<br>info@campercashmate.example</div></div>

  <div class="fh" style="left:760px">Menu</div>
  <ul class="fmenu">
    <li>Home</li><li>About</li><li>FAQ</li><li>Boat Loans</li><li>RV Loans</li><li>Testimonials</li><li>Blog</li><li>Affiliate Program</li><li>Contact</li>
  </ul>

  <div class="fh" style="left:966px">Follow Us</div>
  <div class="fsoc" style="top:3878px"><i></i><div>Follow Us on<br>FRIENDFEEDLY</div></div>
  <div class="fsoc" style="top:3923px"><i></i><div>Follow Us on<br>SNAPGALLERY</div></div>
  <div class="fsoc" style="top:3968px"><i></i><div>Follow Us on<br>WORKLINKR</div></div>

  <div class="fline"></div>
  <div class="totop">GO TO TOP <svg width="10" height="10" viewBox="0 0 10 10"><path d="M5 9V1M1 5l4-4 4 4" stroke="#fff" stroke-width="1.6" fill="none"/></svg></div>
  <div class="copy">© 2024 CamperCashMate &nbsp;|&nbsp; &nbsp;All Rights Reserved</div>
  <div class="tag">C45</div>
</footer>

</body>
</html>
```